Len Morvath

I am the director of Casa Del Humo International. We make premium cigars

I want an insanely beautiful card that directly attracts attention. Do your best. The card can use emboss, foil, laser-cut metal or anything else. Make it stand out, but also elegant.

Target Market(s)

Cigar Distributors

Industry/Entity Type

Cigars

Contact Information for Business Card

Email: len.morvath@morvaths.com + Logos (attached) + Position: Director + 'High-End Cigars'

Colors

Designer to choose colors to be used in the design.

Requirements
Nice to have
• Please check us out at www.casadelhumo.com and try to use our colors and styles

```html
<!DOCTYPE html>
<html lang="en">
<head>
<meta charset="utf-8">
<title>Casa Del Humo International — Business Card</title>
<link rel="stylesheet" href="https://fonts.googleapis.com/css2?family=EB+Garamond:wght@400;500&family=Tinos:wght@400;700&family=Arimo:wght@400&display=swap">
<style>
  :root {
    --backdrop: #1a1a1a;
    --card: #111111;
    --ink-white: #f4f4f4;
    --ink-silver: #c9c9c9;
    --accent-red: #d0112b;
    --rule-red: #b3262f;
  }
  html, body {
    margin: 0;
    padding: 0;
    width: 1200px;
    height: 1059px;
    overflow: hidden;
    background: var(--backdrop);
  }
  .business-card {
    position: absolute;
    left: 172px;
    top: 286px;
    width: 856px;
    height: 487px;
    background: var(--card);
    border-radius: 28px;
    color: var(--ink-white);
  }
  .company-name {
    position: absolute;
    left: 0;
    right: 0;
    top: 56px;
    margin: 0;
    text-align: center;
    font-family: "EB Garamond", serif;
    font-weight: 400;
    font-size: 38px;
    letter-spacing: 0.5px;
    line-height: 1;
  }
  .title-divider {
    position: absolute;
    left: 79px;
    top: 110px;
    width: 698px;
    height: 20px;
  }
  .location {
    position: absolute;
    left: 0;
    right: 0;
    top: 151px;
    margin: 0;
    text-align: center;
    font-family: "Arimo", sans-serif;
    font-size: 26px;
    line-height: 1;
  }
  .person {
    position: absolute;
    left: 45px;
    top: 224px;
  }
  .person-name {
    margin: 0;
    font-family: "Tinos", serif;
    font-weight: 700;
    font-size: 35px;
    line-height: 1;
    color: var(--accent-red);
  }
  .person-role {
    margin: 8px 0 0;
    font-family: "Tinos", serif;
    font-size: 21px;
    line-height: 1;
  }
  .section-rule {
    position: absolute;
    left: 45px;
    top: 318px;
    width: 779px;
    height: 2px;
    background: var(--accent-red);
  }
  .contact-list {
    position: absolute;
    left: 48px;
    top: 346px;
    margin: 0;
    padding: 0;
    list-style: none;
    font-family: "Tinos", serif;
    font-size: 21px;
  }
  .contact-item {
    display: flex;
    align-items: center;
    height: 24px;
    margin-bottom: 16px;
  }
  .contact-icon {
    width: 24px;
    height: 24px;
    margin-right: 14px;
    flex: none;
  }
  .contact-item.phone .contact-icon { margin-right: 12px; }
  .product-lines {
    position: absolute;
    left: 380px;
    top: 380px;
    width: 440px;
    display: flex;
    justify-content: space-between;
    align-items: center;
    font-family: "EB Garamond", serif;
    font-weight: 500;
    font-size: 24px;
    color: var(--ink-silver);
  }
</style>
</head>
<body>
  <main class="business-card">
    <h1 class="company-name">CASA DEL HUMO INTERNATIONAL</h1>
    <svg class="title-divider" viewBox="0 0 698 20" aria-hidden="true">
      <line x1="0" y1="10" x2="698" y2="10" stroke="var(--rule-red)" stroke-width="1.2"/>
      <rect x="342" y="3" width="14" height="14" fill="#d9363e" transform="rotate(45 349 10)"/>
    </svg>
    <p class="location">SANTA LUMBRE - HONDURAS</p>

    <section class="person">
      <h2 class="person-name">Len Morvath</h2>
      <p class="person-role">Managing Director</p>
    </section>

    <div class="section-rule"></div>

    <ul class="contact-list">
      <li class="contact-item phone">
        <svg class="contact-icon" viewBox="0 0 24 24" aria-hidden="true">
          <path d="M6.6 2.5c.5 0 .9.3 1.1.8l1.4 3.6c.2.5 0 1-.4 1.3L7 9.5c1 2.6 3 4.6 5.6 5.6l1.3-1.7c.3-.4.8-.6 1.3-.4l3.6 1.4c.5.2.8.6.8 1.1v3c0 1.1-.9 2-2 2C9.5 20.5 3.5 14.5 3.5 6.4c0-1.1.9-2 2-2z" fill="var(--accent-red)"/>
          <path d="M14 3.5a7 7 0 0 1 6.5 6.5M14 6.8a3.8 3.8 0 0 1 3.2 3.2" stroke="var(--accent-red)" stroke-width="1.8" fill="none" stroke-linecap="round"/>
        </svg>
        <span>+44 7700 900412</span>
      </li>
      <li class="contact-item email">
        <svg class="contact-icon" viewBox="0 0 24 24" aria-hidden="true">
          <rect x="1" y="5" width="22" height="15" fill="var(--accent-red)"/>
          <path d="M1.5 5.5 12 13.5 22.5 5.5" stroke="var(--card)" stroke-width="1.8" fill="none"/>
        </svg>
        <span>len.morvath@morvaths.com</span>
      </li>
      <li class="contact-item web">
        <svg class="contact-icon" viewBox="0 0 24 24" aria-hidden="true">
          <circle cx="12" cy="12" r="10.5" fill="var(--accent-red)"/>
          <path d="M12 1.5v21M1.5 12h21M12 1.5c-3.5 3-3.5 18 0 21M12 1.5c3.5 3 3.5 18 0 21" stroke="var(--card)" stroke-width="1.4" fill="none"/>
        </svg>
        <span>www.casadelhumo.com</span>
      </li>
    </ul>

    <div class="product-lines">
      <span class="product-line">Meridian</span>
      <span class="product-line">Oro Reserve</span>
      <span class="product-line">Serie Carmín</span>
    </div>
  </main>
</body>
</html>
```